Mixed Martial Arts Business Book Cover

Dorian Caskell Jr aka The Dojo Growth Mentor Presents

The name of my book is

"Our Studio Fortune Atlas"

tagline is

"The Anything Goes Manual For Growing Your Combat Gym Into A TRUE Enterprise"

I would like like my image incorporated some how

Target Market(s)

mixed martial arts and brazilian jiu jitsu school owners

Industry/Entity Type

Business

Requirements
Must have
• The image I provided incorporated some how (unless) yiou just think its stupid and wont work
Nice to have
• these guys own schools teach people in the QKT cage fighting so I'm not sure but the qkt cage fence ( a fence look) may be cool, or maybe not but i'm not opposedto seeing a design with a cage/fence also
• nice to have the image i provided if possible
Should not have
• should not have any images of random fighters

```html
<!DOCTYPE html>
<html lang="en">
<head>
<meta charset="utf-8">
<title>Our Studio Fortune Atlas — Book Cover</title>
<link rel="stylesheet" href="https://fonts.googleapis.com/css2?family=Oswald:wght@500;600;700&family=Tinos:wght@700&display=swap">
<style>
  :root{
    --page-bg:#ffffff;
    --navy-deep:#0d1a31;
    --navy-mid:#1a3157;
    --band-blue:#1d3b69;
    --gold:#f6c81b;
    --gold-deep:#e9ad0c;
    --white:#ffffff;
    --rule:#cfd6e2;
    --photo-dark:#161616;
    --photo-mid:#3a3835;
  }
  *{margin:0;padding:0;box-sizing:border-box;}
  html,body{width:1200px;height:1135px;overflow:hidden;background:var(--page-bg);}
  .canvas{position:relative;width:1200px;height:1135px;}
  .book-cover{
    position:absolute;left:264px;top:30px;width:672px;height:1075px;
    background:linear-gradient(180deg,var(--navy-deep) 0%,var(--navy-mid) 52%);
    box-shadow:0 6px 18px rgba(0,0,0,.18);
    overflow:hidden;
  }
  .title-art{position:absolute;left:0;top:0;width:672px;height:560px;}
  .title-main{font-family:"Oswald",sans-serif;font-weight:600;fill:url(#goldFill);}
  .title-sub{font-family:"Oswald",sans-serif;font-weight:500;fill:var(--white);}
  .tagline{
    position:absolute;left:40px;right:40px;top:450px;
    font-family:"Tinos",serif;font-weight:700;color:var(--white);
    font-size:23px;line-height:37px;text-align:center;
  }
  .tagline .accent{color:var(--gold);}
  .gold-rule{position:absolute;left:0;width:100%;height:5px;background:var(--gold);}
  .gold-rule.top{top:559px;}
  .gold-rule.bottom{top:936px;}
  .stage-photo{
    position:absolute;left:0;top:564px;width:100%;height:372px;
    background:linear-gradient(180deg,var(--photo-dark) 0%,var(--photo-mid) 62%,#5a4f45 100%);
  }
  .author-band{
    position:absolute;left:0;top:941px;width:100%;height:134px;
    background:var(--band-blue);
    display:flex;align-items:center;justify-content:center;
  }
  .author-name{
    font-family:"Oswald",sans-serif;font-weight:600;color:var(--white);
    font-size:50px;letter-spacing:14px;text-transform:uppercase;
  }
</style>
</head>
<body>
<div class="canvas">
  <div class="book-cover">
    <svg class="title-art" viewBox="0 0 672 560" xmlns="http://www.w3.org/2000/svg">
      <defs>
        <linearGradient id="goldFill" x1="0" y1="0" x2="0" y2="1">
          <stop offset="0" stop-color="#f8d21f"/>
          <stop offset="1" stop-color="#e9ad0c"/>
        </linearGradient>
      </defs>
      <text class="title-main" x="336" y="205" font-size="170" text-anchor="middle" textLength="560" lengthAdjust="spacingAndGlyphs">OUR STUDIO</text>
      <text class="title-main" x="336" y="345" font-size="160" text-anchor="middle" textLength="560" lengthAdjust="spacingAndGlyphs">FORTUNE</text>
      <line x1="60" y1="392" x2="180" y2="392" stroke="#cfd6e2" stroke-width="2"/>
      <line x1="492" y1="392" x2="612" y2="392" stroke="#cfd6e2" stroke-width="2"/>
      <text class="title-sub" x="336" y="418" font-size="80" text-anchor="middle">ATLAS</text>
      <line x1="60" y1="442" x2="612" y2="442" stroke="#cfd6e2" stroke-width="2"/>
      <line x1="60" y1="535" x2="612" y2="535" stroke="#cfd6e2" stroke-width="2"/>
    </svg>
    <p class="tagline">The Anything Goes Manual For Growing<br>Your Combat Gym Into A <span class="accent">TRUE</span> Enterprise</p>
    <div class="gold-rule top"></div>
    <div class="stage-photo" role="img" aria-label="Photo of the author speaking on stage to a seated audience of school owners"></div>
    <div class="gold-rule bottom"></div>
    <div class="author-band"><span class="author-name">Dorian Caskell Jr</span></div>
  </div>
</div>
</body>
</html>
```